Business Cards For Glintwell
Desmond Kuvetti
Simple
CEO and Founder
2871 Pellfield Ln Brockville Ontario K3P2c8
Desmond@Kuvetti-mail.test
Keep it simple and clean. We want the logo BIG on the one side and company info on the other. If you can get some type of interlock going from bad to restored too that might look nice faded as a background on one of the sides.
750PineRidgeRnR 750PineRidgeRnR
https://www.socialpage.test/750PineRidgeRR/photos/pb.382915067214433.-1109384000.1285719304./517293048116520/?type=3&theater this is a good picture that would be nice to have one one side of the cards faded out
Logo has been uploaded.
Grafto Grafto
kindly upload logo

```html
<!DOCTYPE html>
<html lang="en">
<head>
<meta charset="utf-8">
<title>Glintwell Business Cards</title>
<link rel="stylesheet" href="https://fonts.googleapis.com/css2?family=Open+Sans:wght@400;600;700;800&display=swap">
<style>
  :root {
    --stage: #e9e9ec;
    --card-white: #ffffff;
    --navy: #2f3b85;
    --arc-grey: #4a4a52;
    --ink: #2b2b33;
    --text-light: #ffffff;
  }
  * { box-sizing: border-box; margin: 0; padding: 0; }
  html, body {
    width: 1200px; height: 909px; overflow: hidden;
    background: var(--stage);
    font-family: "Open Sans", sans-serif;
  }
  .stage {
    position: relative; width: 1200px; height: 909px;
    display: flex; justify-content: center; align-items: center; gap: 70px;
  }
  .card {
    position: relative; width: 380px; height: 660px;
    background: var(--card-white);
    box-shadow: 0 8px 24px rgba(0,0,0,0.18);
    overflow: hidden;
  }
  .card__wave { position: absolute; inset: 0; width: 100%; height: 100%; }
  .brand {
    position: absolute; left: 0; right: 0;
    display: flex; justify-content: center; align-items: center; gap: 10px;
  }
  .brand__mark { width: 18px; height: 18px; background: var(--navy); }
  .brand__name {
    font-weight: 800; color: var(--navy); letter-spacing: 0.5px;
  }
  .card--front .brand { top: 118px; }
  .card--front .brand__name { font-size: 38px; }
  .card--back .brand { top: 112px; }
  .card--back .brand__name { font-size: 46px; }

  .contact {
    position: absolute; left: 0; right: 0; top: 330px;
    color: var(--text-light); text-align: center;
    font-size: 16px; line-height: 1.45;
  }
  .contact__name { font-size: 21px; font-weight: 700; }
  .contact__role { font-size: 17px; margin-bottom: 10px; }
  .contact__address { margin-bottom: 8px; }
  .contact__label { font-weight: 700; }

  .card__web {
    position: absolute; right: 26px; bottom: 26px;
    color: var(--text-light); font-size: 13px; letter-spacing: 0.3px;
  }
</style>
</head>
<body>
<main class="stage">
  <article class="card card--front">
    <svg class="card__wave" viewBox="0 0 380 660" preserveAspectRatio="none" aria-hidden="true">
      <path d="M0 250 Q190 330 380 250 L380 660 L0 660 Z" fill="var(--arc-grey)"/>
      <path d="M0 262 Q190 344 380 262 L380 660 L0 660 Z" fill="var(--navy)"/>
    </svg>
    <div class="brand"><span class="brand__mark"></span><span class="brand__name">Glintwell</span></div>
    <div class="contact">
      <p class="contact__name">Desmond Kuvetti</p>
      <p class="contact__role">Consultant</p>
      <p class="contact__address">2871 Pellfield Ln,<br>Brockville Ontario<br>K3P2c8</p>
      <p><span class="contact__label">Ph:</span> 555 014 7788</p>
      <p><span class="contact__label">Cell:</span> 555 014 7788</p>
      <p><span class="contact__label">Fax:</span> 555 014 7788</p>
      <p><span class="contact__label">Email:</span> Desmond@Kuvetti-mail.test</p>
      <p>www.glintwell.test</p>
    </div>
  </article>

  <article class="card card--back">
    <svg class="card__wave" viewBox="0 0 380 660" preserveAspectRatio="none" aria-hidden="true">
      <path d="M0 300 Q200 270 380 160 L380 660 L0 660 Z" fill="var(--arc-grey)"/>
      <path d="M0 314 Q205 284 380 174 L380 660 L0 660 Z" fill="var(--navy)"/>
    </svg>
    <div class="brand"><span class="brand__mark"></span><span class="brand__name">Glintwell</span></div>
    <p class="card__web">www.glintwell.test</p>
  </article>
</main>
</body>
</html>
```